QM Kalorvex.Brendal GmbH needed a letterhead template

For English scroll down. We need a letterhead template and since we already have our logo design successfully with you, we now want to also design the letterhead with you. Down in the uploaded file you see what is important and what should definitely be seen on our template. The template should be like the homepage (www.kalorvex.brendal) held in red, blue and white. We need a letter-head submission. In the bottom in the chapter "databases uploading" you can find the most important things, did must be on the submission. The submission shoulderstand be in the colors blue, red and white like our homepage (www.kalorvex.brendal).

```html
<!DOCTYPE html>
<html lang="en">
<head>
<meta charset="utf-8">
<title>Kalorvex.Brendal Letterhead</title>
<link href="https://fonts.googleapis.com/css2?family=Lato:wght@400;700&display=swap" rel="stylesheet">
<style>
  :root {
    --backdrop: #cfcfcf;
    --paper: #ececec;
    --ink: #2f2f2f;
    --muted: #555;
    --brand-blue: #1a6bb5;
    --brand-red: #c8202a;
    --sign-tone: #c9d8ee;
  }
  html, body {
    margin: 0;
    padding: 0;
    width: 1000px;
    height: 1200px;
    overflow: hidden;
    background: var(--backdrop);
    font-family: "Lato", sans-serif;
  }
  .letter {
    position: absolute;
    left: 76px;
    top: 0;
    width: 848px;
    height: 1200px;
    background: var(--paper);
    color: var(--ink);
  }
  .brand {
    position: absolute;
    left: 58px;
    top: 112px;
    display: flex;
    align-items: center;
    gap: 10px;
  }
  .brand-dot {
    width: 22px;
    height: 22px;
    border-radius: 50%;
    background: var(--brand-red);
  }
  .brand-name {
    font-size: 30px;
    font-weight: 700;
    color: var(--brand-blue);
  }
  .sender {
    position: absolute;
    left: 525px;
    top: 80px;
    font-size: 15px;
    line-height: 22px;
    color: var(--ink);
  }
  .sender p { margin: 0; }
  .contact-list {
    list-style: none;
    margin: 12px 0 0;
    padding: 0;
  }
  .contact-list li {
    display: flex;
    align-items: center;
    gap: 9px;
    line-height: 21px;
  }
  .contact-list svg { width: 15px; height: 15px; flex: none; }
  .salutation {
    position: absolute;
    left: 62px;
    top: 372px;
    margin: 0;
    font-size: 15px;
    font-weight: 700;
  }
  .body-copy {
    position: absolute;
    left: 62px;
    top: 422px;
    width: 745px;
    font-size: 14.2px;
    line-height: 18.6px;
  }
  .body-copy p { margin: 0 0 18px; }
  .closing {
    position: absolute;
    left: 62px;
    top: 797px;
    font-size: 15px;
    line-height: 21px;
  }
  .closing p { margin: 0; }
  .closing .signer { font-weight: 700; }
  .signature {
    position: absolute;
    left: 192px;
    top: 822px;
    width: 130px;
    height: 46px;
    background: var(--sign-tone);
    border-radius: 4px;
  }
  .bank-details {
    position: absolute;
    left: 0;
    right: 0;
    top: 1141px;
    margin: 0;
    text-align: center;
    font-size: 15px;
    color: var(--muted);
  }
</style>
</head>
<body>
  <main class="letter">
    <div class="brand">
      <span class="brand-dot"></span>
      <span class="brand-name">Kalorvex.Brendal</span>
    </div>

    <address class="sender" style="font-style:normal">
      <p>Geschäftsführer Dr. Marenko Lisbeth</p>
      <p>Feldweg 12, 6020 Kalmsdorf, Tirol, Österreich</p>
      <ul class="contact-list">
        <li>
          <svg viewBox="0 0 16 16" aria-hidden="true"><path fill="var(--brand-red)" d="M3 2h3l1 3-2 1.5a9 9 0 0 0 4.5 4.5L11 9l3 1v3a1 1 0 0 1-1 1A12 12 0 0 1 2 3a1 1 0 0 1 1-1z"/></svg>
          0800 55 4190
        </li>
        <li>
          <svg viewBox="0 0 16 16" aria-hidden="true"><rect x="1" y="3.5" width="14" height="9" fill="var(--brand-red)"/><path d="M1.5 4l6.5 5 6.5-5" stroke="#fff" stroke-width="1.2" fill="none"/></svg>
          contact@kalorvex.brendal
        </li>
        <li>
          <svg viewBox="0 0 16 16" aria-hidden="true"><g fill="none" stroke="var(--brand-red)" stroke-width="1.3"><circle cx="8" cy="8" r="6.2"/><ellipse cx="8" cy="8" rx="2.8" ry="6.2"/><path d="M2 8h12M3 5h10M3 11h10"/></g></svg>
          www.kalorvex.brendal
        </li>
      </ul>
    </address>

    <p class="salutation">Dear Mr. Smith,</p>

    <section class="body-copy">
      <p>Lorem ipsum dolor sit amet, consectetur adipiscing elit. Donec orci purus, luctus vitae dignissim eu, iaculis sed purus. Vivamus faucibus, ipsum nec aliquet viverra, leo mauris condimentum ligula, sit amet sagittis enim ligula quis arcu. Nam egestas tortor id nisi porttitor mattis. In tortor ante, ultricies in suscipit a, tempus non massa. Vivamus et auctor mi.</p>
      <p>Fusce vel massa nulla. Phasellus nec eros mauris, et scelerisque orci. Donec malesuada orci vitae nulla accumsan porta a id massa. Quisque accumsan iaculis magna sit amet fringilla. Maecenas consequat, magna eget tincidunt semper, odio nibh rutrum mi, id feugiat ante nisi eu risus. Vestibulum nunc orci, rhoncus a placerat in, ultricies in mi. Cras mattis varius eros, vel fringilla nisi suscipit eget.</p>
      <p>Quisque scelerisque sagittis nulla at porttitor. Mauris a justo et tellus interdum tristique. Sed id augue vitae urna euismod commodo aliquet a quam. Pellentesque arcu velit, cursus et malesuada ut, consequat et diam. Nullam erat sem, rhoncus id ullamcorper vitae, rhoncus et arcu. In ultricies ultricies nulla, ut rutrum nisi iaculis at. Donec eu magna a metus ornare faucibus.</p>
      <p>Fusce aliquet faucibus ultricies. Morbi semper, est id tincidunt gravida, sem arcu adipiscing lacus, ac bibendum nulla leo eu purus. Quisque nec diam sed risus consectetur a ccumsan quis quis nibh. Vestibulum id purus lorem.</p>
    </section>

    <div class="closing">
      <p class="signer">John Doe</p>
      <p>Co-Founder &amp; CEO</p>
    </div>
    <div class="signature" role="img" aria-label="Handwritten signature of John Doe"></div>

    <p class="bank-details">Landbank: 1234 &nbsp;|&nbsp; IBAN: AT12 3456 78901452 &nbsp;|&nbsp; BIC: 2547 &nbsp;|&nbsp; UID-Nr.: ATU25876</p>
  </main>
</body>
</html>
```